KQ Flier and Logo

We need a one-page color marketing consumer flier and a new logo.

Target Market(s)

Seniors

Font styles to use
Sans Serif

Colors
85acd3

Requirements
Must have
• Veteran or Military theme, Benefit amounts.

```html
<!DOCTYPE html>
<html lang="en">
<head>
<meta charset="utf-8">
<title>KQ Veterans Benefits Flier</title>
<link rel="stylesheet" href="https://fonts.googleapis.com/css2?family=Josefin+Sans:wght@300&family=Pathway+Gothic+One&family=Oswald:wght@500;600&display=swap">
<style>
  :root {
    --canvas: #e9e9e9;
    --blue-deep: #1f77c9;
    --blue-mid: #3a93d6;
    --blue-light: #85acd3;
    --gold: #cbb58a;
    --tan-band: #b2a585;
    --tan-light: #cfc4a8;
    --wood-light: #d9c7ad;
    --wood-mid: #bea98c;
    --ink: #262626;
    --white: #ffffff;
    --navy: #1b3c66;
  }
  * { box-sizing: border-box; margin: 0; padding: 0; }
  html, body {
    width: 1200px; height: 1200px; overflow: hidden;
    background: var(--canvas);
  }
  .flier {
    position: absolute; left: 198px; top: 30px;
    width: 804px; height: 1140px; overflow: hidden;
    font-family: "Pathway Gothic One", "Arial Narrow", sans-serif;
    color: var(--ink);
    box-shadow: 0 6px 18px rgba(0,0,0,0.18);
  }
  .hero {
    position: absolute; left: 0; top: 0; width: 804px; height: 498px;
    background: linear-gradient(120deg, var(--blue-deep) 0%, var(--blue-mid) 45%, #4ea6da 70%, #3b93d3 100%);
  }
  .brand {
    position: absolute; left: 61px; top: 24px; width: 208px; height: 208px;
  }
  .brand-name {
    position: absolute; left: 61px; top: 24px; width: 208px; height: 208px;
    display: flex; align-items: center; justify-content: center; text-align: center;
    font-size: 27px; line-height: 1.15; color: var(--navy); padding: 0 30px;
  }
  .title {
    position: absolute; left: 303px; top: 84px; width: 447px;
    font-family: "Josefin Sans", sans-serif; font-weight: 300;
    font-size: 35px; letter-spacing: 3px; color: var(--white); white-space: nowrap;
    text-align: center; overflow: hidden;
  }
  .title-rule {
    position: absolute; left: 303px; top: 131px; width: 447px; height: 3px; background: var(--white);
  }
  .intro {
    position: absolute; left: 303px; top: 150px; width: 460px;
    font-size: 25px; line-height: 31px; color: var(--white);
  }
  .benefit-box {
    position: absolute; top: 259px; width: 329px; height: 204px;
    border: 2px solid var(--white); border-radius: 20px;
    padding: 17px 0 0 11px;
  }
  .benefit-box.left { left: 70px; }
  .benefit-box.right { left: 415px; }
  .benefit-label { font-size: 22px; color: var(--white); letter-spacing: 0.3px; white-space: nowrap; }
  .benefit-amount { font-size: 39px; color: var(--gold); line-height: 44px; margin-bottom: 19px; white-space: nowrap; }
  .cta-band {
    position: absolute; left: 0; top: 498px; width: 804px; height: 38px;
    background: linear-gradient(90deg, var(--tan-band) 0%, var(--tan-light) 50%, var(--tan-band) 100%);
    display: flex; align-items: center; justify-content: center;
    font-family: "Oswald", sans-serif; font-weight: 600; font-size: 21px; letter-spacing: 1px; color: var(--white);
  }
  .details {
    position: absolute; left: 0; top: 536px; width: 804px; height: 604px;
    background: linear-gradient(160deg, var(--wood-light) 0%, #d2bfa2 45%, var(--wood-mid) 100%);
  }
  .col-heading { font-size: 22px; font-weight: 400; }
  .service { position: absolute; left: 86px; top: 560px; width: 292px; }
  .service ul { list-style: none; margin-top: 26px; }
  .service li { font-size: 22px; line-height: 25.5px; padding-left: 5px; }
  .service li::before { content: "\2022"; margin-right: 8px; font-size: 1.1em; }
  .divider { position: absolute; left: 408px; top: 599px; width: 1.5px; height: 413px; background: var(--ink); }
  .criteria { position: absolute; left: 452px; top: 560px; width: 278px; }
  .criterion p { font-size: 22px; line-height: 25.5px; text-align: justify; }
  .criterion.health p { margin-top: 26px; margin-bottom: 12px; }
  .criterion.income { margin-bottom: 22px; }
  .contact { position: absolute; left: 64px; top: 1015px; width: 730px; }
  .contact .name { font-size: 22px; padding-left: 4px; line-height: 24px; }
  .contact .line { font-size: 22px; line-height: 23px; letter-spacing: 0.4px; }
  .disclaimer { font-size: 17px; line-height: 18px; letter-spacing: 0.5px; margin-top: 1px; }
</style>
</head>
<body>
  <div class="flier">
    <div class="hero" role="img" aria-label="Waving blue flag fabric background"></div>

    <svg class="brand" viewBox="0 0 208 208" aria-hidden="true">
      <circle cx="104" cy="104" r="102" fill="#b9d3ea"/>
    </svg>
    <div class="brand-name">Harbor Elder Guidance</div>

    <h1 class="title">VETERANS BENEFITS</h1>
    <div class="title-rule"></div>
    <p class="intro">This benefit can provide a significant monthly income to those who meet the eligibility requirements.</p>

    <div class="benefit-box left">
      <div class="benefit-label">MARRIED VETERAN WITH CARE NEEDS:</div>
      <div class="benefit-amount">UP TO $2,230 / Month</div>
      <div class="benefit-label">SINGLE VETERAN:</div>
      <div class="benefit-amount">UP TO $1,881 / Month</div>
    </div>
    <div class="benefit-box right">
      <div class="benefit-label">SURVIVING SPOUSE:</div>
      <div class="benefit-amount">UP TO $1,209 / Month</div>
      <div class="benefit-label">MARRIED VETERAN ONLY SPOUSE NEEDS CARE:</div>
      <div class="benefit-amount">UP TO $1,442 / Month</div>
    </div>

    <div class="cta-band">CALL TO SET UP AN APPOINTMENT TODAY!</div>

    <div class="details" role="img" aria-label="Military dog tags on chain resting on a wooden floor"></div>

    <section class="service">
      <h2 class="col-heading">ELIGIBILITY REQUIREMENTS SERVICE:</h2>
      <ul>
        <li>World War I</li>
        <li>World War II</li>
        <li>Korean Conflict</li>
        <li>Vietnam Era</li>
        <li>Served in the Republic of Vietnam</li>
        <li>Gulf War</li>
        <li>90 days of active duty service, with at least one day during war time.</li>
        <li>Discharge excluding dishonorable.</li>
      </ul>
    </section>

    <div class="divider"></div>

    <section class="criteria">
      <div class="criterion health">
        <h2 class="col-heading">HEALTH:</h2>
        <p>Disabled and unable to work, or 65+ in need of daily assistance.</p>
      </div>
      <div class="criterion income">
        <h2 class="col-heading">INCOME:</h2>
        <p>Monthly income (after expenses) must be below the maximum benefit limit. Most individuals receiving care on a regular basis meet this qualification.</p>
      </div>
      <div class="criterion worth">
        <h2 class="col-heading">NET WORTH:</h2>
        <p>In 2018, KQ implemented a Bright-Line Net Worth limit but with proper planning most can become eligible. To qualify as a “surviving spouse” you had to have been married to the Veteran until his or her death.</p>
      </div>
    </section>

    <footer class="contact">
      <div class="name">DANIEL HALE CFP®, CRPC®</div>
      <div class="line">4200 Meridian Ave., Ste 300 Austin, TX 78701</div>
      <div class="line">Office: 555-014-2200 Fax: 555-014-2201 Web: www.HEGTEXAS.com</div>
      <p class="disclaimer">*Harbor Elder Guidance of Texas is a private financial services company and not part of the Department of KQ.<br>Benefit is determined by the KQ based on eligibility.</p>
    </footer>
  </div>
</body>
</html>
```